Corporate Design für eine Veranstaltungsagentur
Vielen Dank an Bartholdt, der trotz vieler unserer Revisionswünsche stets freundlich war, professionell und schnell gearbeitet hat und uns am Ende ein wirklich wunderbares Ergebnis geliefert hat! :-) Wir können ihn uneingeschränkt weiterempfehlen!
Zielgruppe
Agentur zur Planung, Organisation und Durchführung von Veranstaltungen aller Art
Ingenieurbetrieb für Veranstaltungstechnik und - produktion
Organisation und Durchführung der 'Nebelklang'-Veranstaltungsreihe: www.nebelklang-turnier.de
Zielgruppe:
Personen jeder Altersgruppe, Privatpersonen, Geschäftskunden
Aufgabenstellung
Die Farbe Grün sollte beibehalten werden.
Logo soll Professionalität und Innovation ausstrahlen, gleichzeitig modern und zeitlos wirken.

```html
<!DOCTYPE html>
<html lang="de">
<head>
<meta charset="utf-8">
<title>Lumera Events – Geschäftsausstattung</title>
<link href="https://fonts.googleapis.com/css2?family=Ubuntu:wght@400;500;700&display=swap" rel="stylesheet">
<style>
  :root{
    --bg:#ecedea;
    --paper:#ffffff;
    --ink:#2b2b2b;
    --muted:#555;
    --green:#5aaf3c;
    --lime:#8dc21f;
    --green-deep:#3fa65a;
    --card-dark:#3a3b39;
    --rule:#c9c9c9;
  }
  *{margin:0;padding:0;box-sizing:border-box}
  html,body{width:1200px;height:856px;overflow:hidden}
  body{background:var(--bg);font-family:"Ubuntu",sans-serif;color:var(--ink);position:relative}

  .letterhead{position:absolute;left:140px;top:136px;width:416px;height:588px;background:var(--paper);box-shadow:0 4px 14px rgba(0,0,0,.18);overflow:hidden}
  .letter-band{position:absolute;left:0;top:0;width:416px;height:588px}
  .brand-mark{position:absolute;right:42px;top:30px;text-align:right}
  .brand-dot{display:block;width:26px;height:26px;border-radius:50%;background:var(--green);margin:0 0 4px auto}
  .brand-name{color:var(--green);font-weight:500;font-size:15px;line-height:14px;letter-spacing:.2px}
  .sender-line{position:absolute;left:45px;top:93px;font-size:4px;color:var(--green);border-bottom:.5px solid var(--green);padding-bottom:1px;width:125px}
  .recipient{position:absolute;left:45px;top:111px;font-size:6px;line-height:8px}
  .recipient .city{margin-top:8px}
  .subject{position:absolute;left:45px;top:201px;font-size:6px;font-weight:700}
  .body-copy{position:absolute;left:45px;top:223px;width:226px;font-size:5.2px;line-height:7.5px;color:var(--ink)}
  .body-copy p{margin-bottom:7px}
  .closing{position:absolute;left:45px;top:420px;font-size:5.2px}
  .signature{position:absolute;left:45px;top:436px;width:90px;height:18px;background:linear-gradient(90deg,#d8d8d8,#eeeeee);border-radius:2px}
  .letter-footer{position:absolute;left:0;bottom:0;width:416px;height:42px;display:flex;justify-content:center;gap:46px;padding-top:11px;color:#fff;font-size:4px;line-height:6px;font-weight:500;text-align:center}
  .letter-footer .contact{text-align:left}

  .card{position:absolute;top:290px;width:163px;height:252px;box-shadow:0 4px 12px rgba(0,0,0,.2)}
  .card-front{left:665px;background:var(--paper);text-align:center}
  .card-front .brand-dot{width:30px;height:30px;margin:26px auto 6px}
  .card-front .brand-name{font-size:19px;line-height:17px}
  .card-rule{width:112px;height:1px;background:var(--rule);margin:20px auto 16px}
  .card-person{font-size:7px;font-weight:500}
  .card-role{font-size:7px;color:var(--green);margin-top:2px}
  .card-details{font-size:7px;line-height:9.5px;margin-top:8px}
  .card-details .gap{margin-top:5px}
  .card-web{font-size:7px;color:var(--green);font-weight:700;margin-top:9px}
  .card-back{left:898px;background:var(--card-dark);display:flex;align-items:center;justify-content:center}
  .card-back .brand-name{color:var(--lime);font-size:18px;line-height:17px;text-align:center}
</style>
</head>
<body>

<section class="letterhead" aria-label="Briefbogen">
  <svg class="letter-band" viewBox="0 0 416 588" aria-hidden="true">
    <defs>
      <linearGradient id="band" x1="0" x2="1" y1="0" y2="0">
        <stop offset="0" stop-color="#8dc21f"/>
        <stop offset="1" stop-color="#3fa65a"/>
      </linearGradient>
    </defs>
    <path d="M0 547 H360 A56 56 0 0 0 416 491 V588 H0 Z" fill="url(#band)"/>
  </svg>

  <div class="brand-mark">
    <span class="brand-dot"></span>
    <div class="brand-name">Lumera<br>Events</div>
  </div>

  <div class="sender-line">Jonas Weidler, Hafenstr. 18, 20457 Hamburg</div>

  <div class="recipient">
    <div>Lena Brandhof</div>
    <div>Lindenweg 27</div>
    <div class="city">10115 Berlin</div>
  </div>

  <div class="subject">Planung Ihrer Veranstaltung, Rückmeldung.</div>

  <div class="body-copy">
    <p>Vielen Dank für Ihre Anfrage und das freundliche Gespräch in der vergangenen Woche. Gern senden wir Ihnen hiermit unser Angebot für die Planung, Organisation und Durchführung Ihrer Veranstaltung. Wir haben alle besprochenen Punkte aufgenommen, von der Auswahl der Räume über Licht und Ton bis zur Betreuung der Gäste vor Ort. Unser Team begleitet Sie dabei von der ersten Idee bis zum letzten Programmpunkt und sorgt für einen reibungslosen Ablauf. Die einzelnen Leistungen finden Sie in der beigefügten Übersicht.</p>
    <p>Für technische Fragen steht Ihnen unser Ingenieurbüro für Veranstaltungstechnik jederzeit zur Verfügung. Gemeinsam stimmen wir Bühne, Beschallung und Beleuchtung genau auf Ihren Anlass ab. Sollten Sie Änderungen wünschen, passen wir das Angebot gern kurzfristig an. Wir freuen uns darauf, Ihre Veranstaltung mit Ihnen zu gestalten, und melden uns in den nächsten Tagen telefonisch, um die weiteren Schritte und einen Termin für die Besichtigung abzustimmen.</p>
  </div>

  <div class="closing">Mit freundlichen Grüßen</div>
  <div class="signature" role="img" aria-label="Handschriftliche Unterschrift"></div>

  <footer class="letter-footer">
    <div>Lumera Events GmbH<br>Hafenstr. 18<br>20457 Hamburg</div>
    <div class="contact">T 040 / 555 018 20<br>F 040 / 555 018 21<br>kontakt@lumera-events.de</div>
    <div>Talbank AG<br>IBAN: DE44 5500 1023 8870<br>BIC: TALBDEHHXXX</div>
  </footer>
</section>

<section class="card card-front" aria-label="Visitenkarte Vorderseite">
  <span class="brand-dot"></span>
  <div class="brand-name">Lumera<br>Events</div>
  <div class="card-rule"></div>
  <div class="card-person">Jonas Weidler</div>
  <div class="card-role">Geschäftsführung</div>
  <div class="card-details">
    <div>Hafenstr. 18</div>
    <div>20457 Hamburg</div>
    <div class="gap">T: 040 / 555 018 20</div>
    <div>F: 040 / 555 018 21</div>
    <div>kontakt@lumera-events.de</div>
  </div>
  <div class="card-web">www.lumera-events.de</div>
</section>

<section class="card card-back" aria-label="Visitenkarte Rückseite">
  <div class="brand-name">Lumera<br>Events</div>
</section>

</body>
</html>
```